Varnel Health new year card

Hi,
I would like a New Year greetings card to send to my customers.

If you need to look at our logo : www.varnelhealth.com

If you want to play with images of our device, see
qirtatherapy.ca

The goal is to have a card to wish a happy new year and we look forward collaborating with them in the new year.

```html
<!DOCTYPE html>
<html lang="en">
<head>
<meta charset="utf-8">
<title>Varnel Health – Happy New Year 2020</title>
<link rel="stylesheet" href="https://fonts.googleapis.com/css2?family=Barlow+Semi+Condensed:wght@600;700&family=Bodoni+Moda:wght@500&family=Great+Vibes&family=Marcellus&display=swap">
<style>
  :root {
    --page: #ffffff;
    --night-core: #4a2b12;
    --night-mid: #2e1e12;
    --night-edge: #1a120c;
    --gold-light: #fff1a0;
    --gold: #d9a520;
    --gold-deep: #7a4e0a;
    --brand-grey: #6e7177;
    --brand-accent: #e8742a;
    --ink-light: #f3ece2;
    --device-tone: #d9dadd;
  }
  * { margin: 0; padding: 0; box-sizing: border-box; }
  html, body {
    width: 1200px; height: 1200px; overflow: hidden;
    background: var(--page);
  }
  .card {
    position: absolute; left: 238px; top: 94px;
    width: 724px; height: 1013px; overflow: hidden;
    background: radial-gradient(ellipse 70% 55% at 50% 52%, var(--night-core) 0%, var(--night-mid) 50%, var(--night-edge) 100%);
  }
  .fireworks-backdrop {
    position: absolute; inset: 0;
    background:
      radial-gradient(circle at 25% 30%, rgba(217,165,32,.12) 0, transparent 22%),
      radial-gradient(circle at 70% 22%, rgba(217,165,32,.12) 0, transparent 24%),
      radial-gradient(circle at 20% 60%, rgba(217,165,32,.10) 0, transparent 20%),
      radial-gradient(circle at 80% 48%, rgba(217,165,32,.10) 0, transparent 18%),
      radial-gradient(circle at 30% 85%, rgba(217,165,32,.12) 0, transparent 24%),
      radial-gradient(circle at 62% 88%, rgba(217,165,32,.10) 0, transparent 20%);
  }
  .brand {
    position: absolute; left: 0; right: 0; top: 90px;
    display: flex; justify-content: center; align-items: center; gap: 14px;
  }
  .brand-mark { width: 34px; height: 34px; background: var(--brand-accent); }
  .brand-name {
    font-family: "Barlow Semi Condensed", sans-serif; font-weight: 700;
    font-size: 58px; line-height: 1; color: var(--brand-grey);
  }
  .gold {
    background: linear-gradient(180deg, var(--gold-light) 0%, var(--gold) 45%, var(--gold-deep) 100%);
    -webkit-background-clip: text; background-clip: text; color: transparent;
    filter: drop-shadow(0 3px 3px rgba(0,0,0,.75));
  }
  .greeting-lead {
    position: absolute; left: 0; right: 0; top: 192px; text-align: center;
    font-family: "Marcellus", serif; font-size: 68px; line-height: 1;
    white-space: nowrap;
  }
  .greeting-script {
    position: absolute; left: 0; right: 0; text-align: center;
    font-family: "Great Vibes", cursive; line-height: 1.1;
    white-space: nowrap;
  }
  .greeting-script.happy-new { top: 268px; font-size: 128px; }
  .greeting-script.year { top: 440px; font-size: 120px; padding-right: 8px; }
  .year-number {
    position: absolute; left: 143px; top: 546px;
    font-family: "Bodoni Moda", serif; font-weight: 500; font-size: 226px; line-height: 1;
    white-space: nowrap;
    transform: scaleX(.84); transform-origin: left top;
  }
  .device-photo {
    position: absolute; left: 566px; top: 690px; width: 150px; height: 240px;
    border-radius: 40px 40px 24px 24px;
    background: linear-gradient(180deg, #eeeff1 0%, var(--device-tone) 60%, #a9abb0 100%);
  }
  .website {
    position: absolute; left: 0; right: 0; top: 952px; text-align: center;
    font-family: "Barlow Semi Condensed", sans-serif; font-weight: 600;
    font-size: 30px; line-height: 1; color: var(--ink-light);
  }
</style>
</head>
<body>
  <main class="card">
    <div class="fireworks-backdrop" role="img" aria-label="Golden fireworks bursts and soft bokeh lights on a dark brown night sky"></div>

    <header class="brand">
      <span class="brand-mark"></span>
      <span class="brand-name">Varnel Health</span>
    </header>

    <p class="greeting-lead gold">Wish You a</p>
    <h1 class="greeting-script happy-new gold">Happy New</h1>
    <p class="greeting-script year gold">Year</p>
    <p class="year-number gold">2020</p>

    <div class="device-photo" role="img" aria-label="Photo of the white neck-worn therapy device with its mouthpiece and cable"></div>

    <footer class="website">www.varnelhealth.com</footer>
  </main>
</body>
</html>
```